Established coffee roaster needs a coffee bag and label design

We need a new coffee bag design! PLEASE SEE THE DOCUMENT UPLOADED FOR DETAILS; COFFEE PACKAGING PROJECT TASK!
Coffee bag template attached. We will also need a pre-printed sticker label for changing coffee information. 3 Sticker label designed for one core coffee bag design. THANK YOU!!!

Went on vacation/holiday

```html
<!DOCTYPE html>
<html lang="en">
<head>
<meta charset="utf-8">
<title>Quiet Harbor Coffee Bag Dieline</title>
<link rel="stylesheet" href="https://fonts.googleapis.com/css2?family=Montserrat:wght@400;500;600&family=Oswald:wght@300;400&display=swap">
<style>
  :root {
    --navy-deep: #263850;
    --navy: #2E415B;
    --blush: #E3D2CB;
    --caramel: #C49A6C;
    --sand: #C2B59B;
    --ink: #000000;
    --paper: #FFFFFF;
    --guide-blue: #1F4FA8;
    --guide-purple: #8E1E8E;
    --bleed-pink: #B0479A;
  }
  html, body {
    margin: 0;
    padding: 0;
    width: 1111px;
    height: 1200px;
    overflow: hidden;
    background: var(--paper);
  }
  .artboard { display: block; width: 1111px; height: 1200px; }
  .swatch-label { font-family: "Oswald", sans-serif; font-weight: 300; font-size: 22px; fill: var(--ink); }
  .dim-label { font-family: "Montserrat", sans-serif; font-size: 11.5px; fill: var(--guide-blue); }
  .panel-name { font-family: "Montserrat", sans-serif; font-size: 11.5px; fill: var(--guide-purple); }
  .dim-line { stroke: var(--guide-blue); stroke-width: 0.9; fill: none; }
  .panel { fill: var(--navy); }
  .fold { stroke: var(--guide-purple); stroke-width: 0.6; fill: none; }
  .safe { stroke: var(--bleed-pink); stroke-width: 0.5; stroke-dasharray: 4 3; fill: none; opacity: 0.8; }
  .brand { font-family: "Montserrat", sans-serif; font-weight: 500; fill: var(--paper); }
  .copy { font-family: "Montserrat", sans-serif; font-weight: 400; fill: var(--paper); }
  .label-title { font-family: "Montserrat", sans-serif; font-weight: 500; font-size: 18px; fill: var(--ink); }
  .label-field { font-family: "Montserrat", sans-serif; font-weight: 400; font-size: 7.5px; fill: var(--ink); }
  .zipper-band { fill: var(--guide-purple); opacity: 0.35; }
  .zipper-line { stroke: var(--guide-purple); stroke-width: 2; }
</style>
</head>
<body>
<svg class="artboard" viewBox="0 0 1111 1200" xmlns="http://www.w3.org/2000/svg">
  <defs>
    <marker id="arrow" viewBox="0 0 10 10" refX="9" refY="5" markerWidth="7" markerHeight="7" orient="auto-start-reverse">
      <path d="M0 1 L9 5 L0 9" fill="none" stroke="#1F4FA8" stroke-width="1.2"/>
    </marker>
  </defs>

  <!-- Colour palette -->
  <g class="palette">
    <rect x="73" y="69" width="87" height="58" fill="var(--navy-deep)"/>
    <rect x="185" y="69" width="87" height="58" fill="var(--navy)"/>
    <rect x="297" y="68" width="87" height="59" fill="var(--blush)"/>
    <rect x="409" y="68" width="87" height="59" fill="var(--caramel)"/>
    <rect x="521" y="68" width="87" height="59" fill="var(--sand)"/>
    <rect x="633" y="68" width="87" height="59" fill="var(--ink)"/>
    <rect x="745.5" y="68.5" width="87" height="59" fill="var(--paper)" stroke="#000" stroke-width="1"/>
    <text class="swatch-label" x="110" y="155" text-anchor="middle">263850</text>
    <text class="swatch-label" x="227" y="155" text-anchor="middle">2E415B</text>
    <text class="swatch-label" x="338" y="155" text-anchor="middle">E3D2CB</text>
    <text class="swatch-label" x="456" y="155" text-anchor="middle">C49A6C</text>
    <text class="swatch-label" x="567" y="155" text-anchor="middle">C2B59B</text>
    <text class="swatch-label" x="682" y="155" text-anchor="middle">BLACK</text>
    <text class="swatch-label" x="797" y="155" text-anchor="middle">WHITE</text>
  </g>

  <!-- Panel dimensions -->
  <g class="dimensions">
    <text class="panel-name" x="168" y="211" text-anchor="middle">Left</text>
    <text class="panel-name" x="421" y="211" text-anchor="middle">Front</text>
    <text class="panel-name" x="652" y="211" text-anchor="middle">Right</text>
    <text class="panel-name" x="904" y="211" text-anchor="middle">Back</text>
    <line class="dim-line" x1="70" y1="222" x2="140" y2="222" marker-start="url(#arrow)"/>
    <line class="dim-line" x1="193" y1="222" x2="275" y2="222" marker-end="url(#arrow)"/>
    <text class="dim-label" x="167" y="229" text-anchor="middle">85 mm</text>
    <line class="dim-line" x1="275" y1="222" x2="392" y2="222" marker-start="url(#arrow)"/>
    <line class="dim-line" x1="451" y1="222" x2="555" y2="222" marker-end="url(#arrow)"/>
    <text class="dim-label" x="421" y="229" text-anchor="middle">115 mm</text>
    <line class="dim-line" x1="555" y1="222" x2="625" y2="222" marker-start="url(#arrow)"/>
    <line class="dim-line" x1="679" y1="222" x2="761" y2="222" marker-end="url(#arrow)"/>
    <text class="dim-label" x="652" y="229" text-anchor="middle">85 mm</text>
    <line class="dim-line" x1="761" y1="222" x2="876" y2="222" marker-start="url(#arrow)"/>
    <line class="dim-line" x1="936" y1="222" x2="1041" y2="222" marker-end="url(#arrow)"/>
    <text class="dim-label" x="906" y="229" text-anchor="middle">115 mm</text>
    <line class="dim-line" x1="70" y1="215" x2="70" y2="236"/>
    <line class="dim-line" x1="275" y1="215" x2="275" y2="236"/>
    <line class="dim-line" x1="555" y1="215" x2="555" y2="236"/>
    <line class="dim-line" x1="761" y1="215" x2="761" y2="236"/>
    <line class="dim-line" x1="1041" y1="215" x2="1041" y2="236"/>

    <line class="dim-line" x1="49" y1="233" x2="80" y2="233"/>
    <line class="dim-line" x1="49" y1="721" x2="80" y2="721"/>
    <line class="dim-line" x1="57" y1="233" x2="57" y2="438" marker-start="url(#arrow)"/>
    <line class="dim-line" x1="57" y1="490" x2="57" y2="721" marker-end="url(#arrow)"/>
    <text class="dim-label" transform="translate(62 464) rotate(-90)" text-anchor="middle">203 mm</text>

    <line class="dim-line" x1="1041" y1="233" x2="1070" y2="233"/>
    <line class="dim-line" x1="1041" y1="305" x2="1070" y2="305"/>
    <line class="dim-line" x1="1048" y1="233" x2="1048" y2="305"/>
    <text class="dim-label" transform="translate(1065 271) rotate(-90)" text-anchor="middle">30mm</text>
    <line class="dim-line" x1="1043" y1="322" x2="1052" y2="331" marker-end="url(#arrow)"/>
    <text class="dim-label" x="1055" y="336">Zipper</text>

    <line class="dim-line" x1="265" y1="926" x2="290" y2="926"/>
    <line class="dim-line" x1="265" y1="723" x2="265" y2="798" marker-start="url(#arrow)"/>
    <line class="dim-line" x1="265" y1="846" x2="265" y2="926" marker-end="url(#arrow)"/>
    <text class="dim-label" transform="translate(270 820) rotate(-90)" text-anchor="middle">85 mm</text>
  </g>

  <!-- Bag panels (diamond argyle pattern area) -->
  <g class="bag">
    <rect class="panel" x="70" y="233" width="971" height="488" role="img" aria-label="Navy argyle diamond pattern across all bag panels"/>
    <path class="panel" d="M275 721 H555 V914 a12 12 0 0 1 -12 12 H287 a12 12 0 0 1 -12 -12 Z" role="img" aria-label="Navy argyle diamond pattern on bottom gusset"/>
    <rect class="fold" x="70" y="233" width="971" height="488"/>
    <line class="fold" x1="275" y1="233" x2="275" y2="721"/>
    <line class="fold" x1="555" y1="233" x2="555" y2="721"/>
    <line class="fold" x1="761" y1="233" x2="761" y2="721"/>
    <path class="fold" d="M275 721 H555 V914 a12 12 0 0 1 -12 12 H287 a12 12 0 0 1 -12 -12 Z"/>

    <rect class="safe" x="85" y="233" width="175" height="473"/>
    <rect class="safe" x="291" y="233" width="248" height="473"/>
    <rect class="safe" x="570" y="233" width="176" height="473"/>
    <rect class="safe" x="777" y="233" width="248" height="473"/>
    <rect class="safe" x="291" y="737" width="248" height="174"/>

    <text class="dim-label" x="112" y="718" font-size="10" opacity="0.7">6.5mm</text>
    <text class="dim-label" transform="translate(83 700) rotate(-90)" font-size="10" opacity="0.7">6.5mm</text>
  </g>

  <!-- Front panel -->
  <g class="front">
    <circle cx="420" cy="375" r="36" fill="none" stroke="var(--paper)" stroke-width="3"/>
    <text class="brand" x="421" y="445" text-anchor="middle" font-size="23">QUIET HARBOR</text>
    <text class="brand" x="421" y="467" text-anchor="middle" font-size="19.5">COFFEE ROASTERS</text>
    <text class="copy" x="421" y="480" text-anchor="middle" font-size="10.5" letter-spacing="4.6">SINGLE ORIGIN COFFEE</text>

    <g class="flavour-label">
      <rect x="319" y="526" width="193" height="130" rx="14" fill="var(--blush)"/>
      <rect x="324" y="531" width="183" height="120" rx="10" fill="none" stroke="var(--ink)" stroke-width="1.1"/>
      <circle cx="357" cy="557" r="16" fill="var(--ink)" role="img" aria-label="Gratitude flavour mark"/>
      <text class="label-title" x="384" y="553">GRATITUDE</text>
      <text class="label-title" x="384" y="575">FLAVOUR</text>
      <text class="label-field" x="332" y="601">PROCESS:</text>
      <text class="label-field" x="332" y="638">BEST  BEFORE:</text>
    </g>
    <text class="copy" x="446" y="686" font-size="7.5">NET  WEIGHT  :  <tspan font-size="6.5">12oz</tspan></text>
  </g>

  <!-- Back panel -->
  <g class="back">
    <rect class="zipper-band" x="783" y="291" width="258" height="52"/>
    <line class="zipper-line" x1="783" y1="305" x2="1041" y2="305"/>
    <path d="M765 285 a8 8 0 0 1 0 18 a8 8 0 0 1 0 24 v-42 Z" fill="var(--guide-purple)" opacity="0.45"/>
    <line class="dim-line" x1="899" y1="236" x2="899" y2="388" opacity="0.6" marker-start="url(#arrow)" marker-end="url(#arrow)"/>
    <circle cx="899" cy="389" r="27" fill="none" stroke="var(--guide-blue)" stroke-width="0.8" opacity="0.6"/>
    <text class="dim-label" x="897" y="407" text-anchor="middle" font-size="7" opacity="0.6">Valve 65 mm</text>

    <g class="story-card">
      <rect x="799" y="418" width="205" height="243" rx="10" fill="none" stroke="var(--paper)" stroke-width="1"/>
      <circle cx="901" cy="462" r="22" fill="none" stroke="var(--paper)" stroke-width="2.5"/>
      <text class="brand" x="901" y="502" text-anchor="middle" font-size="14">QUIET HARBOR</text>
      <text class="brand" x="901" y="515" text-anchor="middle" font-size="12">COFFEE ROASTERS</text>
      <text class="copy" font-size="5.6">
        <tspan x="804" y="543">QUIET  HARBOR  SINGLE  ORIGIN  COFFEE  OFFERS  A  PURE,</tspan>
        <tspan x="804" y="550">HAND-CRAFTED  EXPERIENCE  FROM  FARM  TO  CUP.</tspan>
        <tspan x="804" y="565">VALUES:  OUR  CORE  VALUES,  COMPASSION,  GRATITUDE,</tspan>
        <tspan x="804" y="572">HONESTY,  HUMILITY,  KINDNESS,  FORGIVENESS,  AND</tspan>
        <tspan x="804" y="579">PATIENCE  ARE  IDEALS  THAT  WE  STRIVE  FOR.  EMBRACE  A</tspan>
        <tspan x="804" y="586">VALUE  AND  MOVE  FORWARD  WITH  YOUR  DAILY  LIFE  IN  A</tspan>
        <tspan x="804" y="593">POSITIVE  WAY!</tspan>
        <tspan x="804" y="616">WEBSITE  ADDRESS:  WWW.QUIETHARBORCOFFEE.COM</tspan>
        <tspan x="804" y="630">@QUIETHARBORCOFFEE</tspan>
        <tspan x="804" y="648">ESTABLISHED  2012</tspan>
        <tspan x="804" y="655">HARBOR FALLS,  MAINE</tspan>
      </text>
    </g>
  </g>

  <!-- Bottom gusset -->
  <g class="bottom">
    <rect x="367" y="743" width="97" height="60" fill="var(--paper)"/>
    <rect x="331" y="815" width="36" height="32" rx="4" fill="var(--paper)" opacity="0.85" role="img" aria-label="Recycling symbol"/>
    <rect x="468" y="815" width="34" height="40" rx="4" fill="var(--paper)" opacity="0.85" role="img" aria-label="Dispose in bin symbol"/>
    <text class="copy" x="416" y="875" text-anchor="middle" font-size="7">HELP  PROTECT  ALL  LIVING  THINGS,  AND  PLEASE</text>
    <text class="copy" x="416" y="884" text-anchor="middle" font-size="7">RECYCLE  THIS  BAG  AFTER  USE</text>
  </g>

  <!-- Sticker variants -->
  <g class="sticker kindness">
    <rect x="94" y="959" width="279" height="204" rx="12" fill="var(--navy)" role="img" aria-label="Navy argyle diamond pattern sticker backing"/>
    <rect x="137" y="996" width="194" height="131" rx="14" fill="var(--caramel)"/>
    <rect x="142" y="1001" width="184" height="121" rx="10" fill="none" stroke="var(--ink)" stroke-width="1.1"/>
    <circle cx="176" cy="1027" r="17" fill="var(--ink)" role="img" aria-label="Kindness flavour mark"/>
    <text class="label-title" x="203" y="1023">KINDNESS</text>
    <text class="label-title" x="203" y="1045">FLAVOUR</text>
    <text class="label-field" x="150" y="1071">PROCESS:</text>
    <text class="label-field" x="150" y="1108">BEST  BEFORE:</text>
  </g>
  <g class="sticker patience">
    <rect x="411" y="959" width="279" height="204" rx="12" fill="var(--navy)" role="img" aria-label="Navy argyle diamond pattern sticker backing"/>
    <rect x="454" y="996" width="194" height="131" rx="14" fill="var(--sand)"/>
    <rect x="459" y="1001" width="184" height="121" rx="10" fill="none" stroke="var(--ink)" stroke-width="1.1"/>
    <circle cx="493" cy="1027" r="19" fill="var(--ink)" role="img" aria-label="Patience flavour mark"/>
    <text class="label-title" x="520" y="1023">PATIENCE</text>
    <text class="label-title" x="520" y="1045">FLAVOUR</text>
    <text class="label-field" x="467" y="1071">PROCESS:</text>
    <text class="label-field" x="467" y="1108">BEST  BEFORE:</text>
  </g>
</svg>
</body>
</html>
```